Website Design for a DJ Entertainment and Productions Comany

We are a full service DJ Entertainment and Productions company looking to have a strong presence in our local market and need a phenomenal website design to drive clients to the site but then also keep them there. We cater to all types of different events varying from weddings to proms to corporate events, birthdays, bar mitzvah's and so on and so on. We also do full lighting for any type of event and we also offer a photobooth service for various events. The best way to get an idea of the services that we offer is to visit http://www.velmorahaus.com/index.html This site is NOT our own but only linked as an example of what we do and will give you an overall overview of what we offer.
We are looking for pure creativity as there are multiple facets to our company and the services we offer. On the one hand we can provide a night club party atmosphere for Proms or dances but on the other hand we also provide professional full service emcee/DJ for weddings and formal events. The key for this site would be to have the pages for each category match the look and feel of the actual service provided, ie the Wedding page will look more refined and professional vs the Party DJ page. Each page needs to fit the overall feel of the Company and Logo though. Here is a list of pages that we would need to have on the final site.
HOME PAGE
PROFESSINAL DJS- This will have info. and pricing of our DJ services for everything but weddings. Should have pics and videos somewhere on this page.
WEDDINGS- All wedding package pricing and info. This page should look more elegant, formal and high class compared to the other pages.
PHOTOBOOTH-Page with info, pricing on photobooth see http://www.glintrivuphotobooth.com/
LIGHTING DESIGN-Info on our lighting services along with pricing
CORPORATE EVENTS-Info on services and pricing for corporate events. This page should seem more professional centered towards business clientele.
CLIENT LOGIN-Page for existing clients to logon to update info and fill out information.
CONNECT WITH US- Social Media links.
Our logo was submitted through Pixel Harbor but I am open to suggestions on revisions if you feel the need to change it. Color is also not set in stone.
I have increased my budget $200 more. Please submit your designs for review, deadline is approaching quickly. Also see brief for revisions.
Thank you.
Target Market(s)
Broad Range but usually Under 40
Industry/Entity Type
Night Club
Look and feel

```html
<!DOCTYPE html>
<html lang="en">
<head>
<meta charset="utf-8">
<title>Vantor Entertainment &amp; Productions – Event Design</title>
<link rel="stylesheet" href="https://fonts.googleapis.com/css2?family=Montserrat:wght@400;600;700&family=Great+Vibes&display=swap">
<style>
:root{
  --red:#e3141f;
  --white:#ffffff;
  --text:#e9eef5;
  --ink:#000000;
  --navy:#0b2748;
  --deep:#05121f;
  --dot:#c9ccd1;
}
*{margin:0;padding:0;box-sizing:border-box}
html,body{width:1200px;height:744px;overflow:hidden;background:var(--ink)}
body{font-family:"Montserrat",sans-serif;color:var(--text);position:relative}
.site-header{position:absolute;left:0;top:0;width:1200px;height:122px;
  background:radial-gradient(ellipse 420px 160px at 300px 60px,#0f3a5a 0%,#071a2a 55%,#000 100%)}
.brand{position:absolute;left:248px;top:30px;display:flex;align-items:center;gap:10px}
.brand-mark{width:40px;height:40px;border-radius:50%;background:var(--red)}
.brand-name{font-weight:700;font-size:15px;line-height:17px;color:var(--red);text-transform:uppercase;letter-spacing:.5px}
.login{position:absolute;right:152px;top:42px;font-weight:700;font-size:14px;color:var(--red);text-decoration:none}
.main-nav{position:absolute;left:249px;top:96px;width:800px;display:flex;justify-content:space-between}
.main-nav a{font-size:12px;color:var(--white);text-decoration:none;letter-spacing:.2px}
.main-nav a.is-active{color:var(--red)}
.hero{position:absolute;left:0;top:122px;width:1200px;height:519px}
.hero-backdrop{position:absolute;inset:0;
  background:radial-gradient(ellipse 500px 300px at 900px 420px,#3b6aa8 0%,rgba(30,70,130,.6) 50%,transparent 100%),
  linear-gradient(90deg,#0a1c3a 0%,#1f4a8a 35%,#2b5aa0 60%,#153566 100%)}
.page-title{position:absolute;left:243px;top:65px;display:flex;align-items:baseline;color:var(--white)}
.page-title .script{font-family:"Great Vibes",cursive;font-size:50px;line-height:1}
.page-title .caps{font-size:26px;font-weight:400;margin-left:-4px;letter-spacing:.5px}
.intro{position:absolute;left:242px;top:148px;width:372px;font-size:11.2px;line-height:16px}
.intro p{margin-bottom:16px}
.intro .contact-lead{margin-left:-2px;margin-bottom:5px}
.intro .email{display:block;margin-left:-2px;color:var(--red);font-size:12.5px;text-decoration:none}
.slide{position:absolute;left:644px;top:148px;width:396px;height:241px;
  background:radial-gradient(ellipse 200px 90px at 300px 40px,#d7b060 0%,transparent 100%),
  linear-gradient(180deg,#6b5424 0%,#9a8552 45%,#c9b98c 75%,#8c7a4e 100%)}
.slide-dots{position:absolute;left:831px;top:400px;display:flex;gap:4px}
.slide-dots span{width:8px;height:8px;border-radius:50%;background:var(--dot)}
.slide-dots span.is-current{background:var(--red)}
.site-footer{position:absolute;left:0;top:641px;width:1200px;height:103px;
  background:radial-gradient(ellipse 360px 140px at 420px 110px,#0d3556 0%,#051522 60%,#000 100%);
  border-top:2px solid #0a0f14}
.book{position:absolute;left:240px;top:15px;font-size:19.5px;color:var(--white)}
.book .cta{color:var(--red)}
.copyright{position:absolute;left:239px;top:49px;font-size:9.4px;color:var(--white)}
.follow{position:absolute;right:159px;top:18px;display:flex;align-items:center;gap:8px}
.follow-label{font-weight:700;font-size:12.5px;color:var(--white);letter-spacing:.5px;margin-right:2px}
.social{width:24px;height:24px;border-radius:4px;display:block}
.social-one{background:#2d5aa8}
.social-two{background:#3fb4e6}
</style>
</head>
<body>
<header class="site-header">
  <div class="brand"><span class="brand-mark"></span><span class="brand-name">Vantor<br>Entertainment &amp; Productions</span></div>
  <a class="login" href="#">Login</a>
  <nav class="main-nav">
    <a href="#">PROFESSIONAL DJS</a>
    <a href="#">WEDDINGS</a>
    <a href="#">PHOTOBOOTH</a>
    <a href="#">LIGHTING DESIGN</a>
    <a href="#" class="is-active">CORPORATE EVENTS</a>
    <a href="#">EVENT DESIGN</a>
  </nav>
</header>
<main class="hero">
  <div class="hero-backdrop" role="img" aria-label="Blue-lit banquet hall with guests and stage lighting"></div>
  <h1 class="page-title"><span class="script">Event</span><span class="caps">DESIGN</span></h1>
  <div class="intro">
    <p>The party everyone will talk about, we're talking about yours. Nightfall Party DJs provides modern DJs in Michigan for big and small events. You deserve more than just music, so we will give you fun options that will keep your dance floor packed. Log online and drag and drop songs with your online party planner.</p>
    <p>Your guests get Queue Up access so they can request songs months in advance. And how cool is it for them to download photos from your Spark Snap Photo Album. Share the fun and experience the difference, you will get more value with our unique options. Do you want more information about a Fun Michigan DJ company? Please click the logo below and take your first step towards the best event ever.</p>
    <p class="contact-lead">Feel free to contact us to book a consultation.</p>
    <a class="email" href="#">DJS@VANTORENTERTAINMENT.COM</a>
  </div>
  <div class="slide" role="img" aria-label="Elegant banquet table set with folded napkins, plates and glasses under warm lights"></div>
  <div class="slide-dots"><span></span><span></span><span class="is-current"></span><span></span><span></span></div>
</main>
<footer class="site-footer">
  <div class="book"><span class="cta">BOOK NOW</span> 555.014.2290</div>
  <div class="copyright">© 2011 VANTOR ENTERTAINMENT &amp; PRODUCTIONS</div>
  <div class="follow"><span class="follow-label">FOLLOW US:</span><a class="social social-one" href="#" aria-label="Social profile one"></a><a class="social social-two" href="#" aria-label="Social profile two"></a></div>
</footer>
</body>
</html>
```